KORVELTA Corporate Business Card

Modern business card design for company which focuses in the areas of Staffing, IT Consulting & Data Services. Please note: We are no longer using the IT subscript on the logo. All designs should have IT subscript removed.
Website: www.korveltait.example

```html
<!DOCTYPE html>
<html lang="en">
<head>
<meta charset="utf-8">
<title>KORVELTA Business Card</title>
<link href="https://fonts.googleapis.com/css2?family=Lato:wght@400;700;900&display=swap" rel="stylesheet">
<style>
  :root {
    --page-bg: #2b2b2b;
    --brand-blue: #0a5c96;
    --bright-blue: #1e9ad6;
    --navy: #134f8c;
    --ink: #2a2a2a;
    --paper: #ffffff;
  }
  * { margin: 0; padding: 0; box-sizing: border-box; }
  html, body {
    width: 1200px; height: 878px; overflow: hidden;
    background: var(--page-bg);
    font-family: "Lato", Arial, sans-serif;
  }
  .stage {
    position: relative; width: 1200px; height: 878px;
  }
  .card {
    position: absolute; left: 320px;
    width: 560px; height: 320px;
    box-shadow: 0 10px 30px rgba(0,0,0,.45);
    overflow: hidden;
  }
  .card-front { top: 70px; background: var(--brand-blue); }
  .card-back { top: 488px; background: var(--paper); }

  .front-mark {
    position: absolute; left: 30px; top: 60px;
    width: 200px; height: 200px; border-radius: 28px;
    background: rgba(255,255,255,.06);
  }
  .front-logo {
    position: absolute; inset: 0;
    display: flex; align-items: center; justify-content: center; gap: 14px;
    color: var(--paper);
  }
  .logo-square {
    width: 34px; height: 34px; border-radius: 6px; background: currentColor;
  }
  .logo-name {
    font-weight: 900; font-size: 52px; letter-spacing: 1px; line-height: 1;
  }

  .back-logo {
    position: absolute; left: 34px; top: 34px;
    display: flex; align-items: center; gap: 10px;
    color: var(--bright-blue);
  }
  .back-logo .logo-square { width: 28px; height: 28px; }
  .back-logo .logo-name { font-size: 44px; }

  .address {
    position: absolute; left: 34px; top: 150px;
    color: var(--bright-blue); font-weight: 700; font-size: 16px; line-height: 1.35;
  }
  .contacts {
    position: absolute; left: 34px; top: 208px;
    list-style: none; color: var(--ink); font-size: 16px;
  }
  .contacts li { display: flex; align-items: center; gap: 14px; height: 24px; }
  .contacts svg { width: 16px; height: 16px; fill: var(--navy); flex: none; }

  .person {
    position: absolute; right: 34px; bottom: 48px; text-align: right;
  }
  .person-name {
    color: var(--navy); font-weight: 900; font-size: 30px; letter-spacing: .5px; line-height: 1.05;
  }
  .person-title { color: var(--bright-blue); font-size: 18px; }
</style>
</head>
<body>
<main class="stage">
  <section class="card card-front" aria-label="Card front">
    <div class="front-mark"></div>
    <div class="front-logo">
      <span class="logo-square"></span>
      <span class="logo-name">KORVELTA</span>
    </div>
  </section>

  <section class="card card-back" aria-label="Card back">
    <div class="back-logo">
      <span class="logo-square"></span>
      <span class="logo-name">KORVELTA</span>
    </div>

    <p class="address">418 Harlow Ave.<br>Brennick, IN 40021</p>

    <ul class="contacts">
      <li>
        <svg viewBox="0 0 24 24" aria-hidden="true"><path d="M6.6 10.8a15 15 0 0 0 6.6 6.6l2.2-2.2a1 1 0 0 1 1-.25 11.4 11.4 0 0 0 3.6.57 1 1 0 0 1 1 1V20a1 1 0 0 1-1 1A17 17 0 0 1 3 4a1 1 0 0 1 1-1h3.5a1 1 0 0 1 1 1c0 1.25.2 2.45.57 3.57a1 1 0 0 1-.25 1z"/></svg>
        <span>555-013-4821</span>
      </li>
      <li>
        <svg viewBox="0 0 24 24" aria-hidden="true"><path d="M2 5h20v14H2zm2 2v.5l8 5 8-5V7l-8 5z"/></svg>
        <span>contactus@korveltait.example</span>
      </li>
      <li>
        <svg viewBox="0 0 24 24" aria-hidden="true"><path d="M12 2a10 10 0 1 0 0 20 10 10 0 0 0 0-20zm6.9 9h-3a15 15 0 0 0-1.4-6A8 8 0 0 1 18.9 11zM12 4c.9 1.3 1.7 3.8 1.9 7h-3.8c.2-3.2 1-5.7 1.9-7zM9.5 5a15 15 0 0 0-1.4 6h-3A8 8 0 0 1 9.5 5zM5.1 13h3a15 15 0 0 0 1.4 6A8 8 0 0 1 5.1 13zM12 20c-.9-1.3-1.7-3.8-1.9-7h3.8c-.2 3.2-1 5.7-1.9 7zm2.5-1a15 15 0 0 0 1.4-6h3a8 8 0 0 1-4.4 6z"/></svg>
        <span>www.korveltait.example</span>
      </li>
    </ul>

    <div class="person">
      <p class="person-name">DANIEL REYES</p>
      <p class="person-title">Founder &amp; CEO</p>
    </div>
  </section>
</main>
</body>
</html>
```